PACKAGING DESIGN - HOT New Brand of Haircare

We are creating a NEW haircare brand that will need to stand out on retail shelves. This is a luxury product at an affordable price. We will look for designs for 2 different formulas - Shine Boosting Shampoo & Moisturizing Conditioner containing Argan Oil and the other will be a Nourishing Shampoo & Hydrating Conditioner containing Coconut Oil.Packaging will be 32 oz bottle with pump (either Boston Round or Bullet shape). Examples are shown on the brief. This product will be sold at national retailers and needs to look like a brand that is sold at a high end boutique or salon.
Updates

Need extra days to review

Target Market(s)

Women and Men 20s - 40s who want high end hair care

Font styles to use
Sans Serif

Colors

Designer to choose colors to be used in the design.

Requirements
Must have
• Label design for the existing bottle - 4 different SKUs. (see attached brief)

```html
<!DOCTYPE html>
<html lang="en">
<head>
<meta charset="utf-8">
<title>Amber Vale – Shine Boosting Shampoo Label</title>
<link rel="stylesheet" href="https://fonts.googleapis.com/css2?family=Libre+Baskerville:wght@400&display=swap">
<style>
  :root {
    --backdrop: #fcd8c2;
    --label-green: #72c4a5;
    --label-green-light: #7fcbae;
    --copper: #b8733f;
    --navy: #27385f;
    --ink-dark: #1f2b2a;
  }
  html, body {
    margin: 0;
    padding: 0;
    width: 932px;
    height: 1200px;
    overflow: hidden;
    background: var(--backdrop);
  }
  .canvas {
    position: relative;
    width: 932px;
    height: 1200px;
    background: var(--backdrop);
  }
  .label {
    position: absolute;
    left: 191px;
    top: 25px;
    width: 550px;
    height: 1150px;
    background: linear-gradient(90deg, var(--label-green) 0%, var(--label-green-light) 45%, var(--label-green) 100%);
    font-family: "Libre Baskerville", Georgia, serif;
    line-height: 1;
  }
  .label__top-band {
    position: absolute;
    left: 0; top: 0;
    width: 100%;
    height: 9px;
    background: var(--copper);
  }
  .brand-name {
    position: absolute;
    left: 73px;
    margin: 0;
    color: var(--copper);
    font-weight: 400;
    white-space: nowrap;
  }
  .brand-name--first { top: 280px; font-size: 48px; letter-spacing: 1px; }
  .brand-name--second { top: 321px; font-size: 94px; }
  .product-title {
    position: absolute;
    left: 59px;
    margin: 0;
    color: var(--navy);
    font-weight: 400;
    white-space: nowrap;
  }
  .product-title--shine { top: 517px; font-size: 96px; }
  .product-title--boosting { top: 598px; font-size: 62px; }
  .product-title--type { top: 663px; font-size: 58px; }
  .divider {
    position: absolute;
    left: 59px;
    top: 759px;
    width: 286px;
    height: 4px;
    background: var(--copper);
  }
  .spec {
    position: absolute;
    left: 59px;
    margin: 0;
    font-size: 25px;
    color: var(--ink-dark);
    white-space: nowrap;
  }
  .spec--ingredient { top: 837px; }
  .spec--hair-a { top: 883px; }
  .spec--hair-b { top: 927px; }
  .spec-rule {
    position: absolute;
    left: 59px;
    top: 868px;
    width: 282px;
    height: 2px;
    background: var(--ink-dark);
  }
  .free-from-seal {
    position: absolute;
    left: 383px;
    top: 924px;
    width: 106px;
    height: 106px;
  }
  .volume {
    position: absolute;
    left: 0;
    top: 1095px;
    width: 100%;
    margin: 0;
    text-align: center;
    font-size: 24px;
    color: var(--ink-dark);
  }
</style>
</head>
<body>
<div class="canvas">
  <section class="label">
    <div class="label__top-band"></div>

    <p class="brand-name brand-name--first">AMBER</p>
    <p class="brand-name brand-name--second">VALE</p>

    <h1 class="product-title product-title--shine">SHINE</h1>
    <p class="product-title product-title--boosting">BOOSTING</p>
    <p class="product-title product-title--type">Shampoo</p>

    <div class="divider"></div>

    <p class="spec spec--ingredient">WITH ARGAN OIL</p>
    <div class="spec-rule"></div>
    <p class="spec spec--hair-a">DRY TO NORMAL</p>
    <p class="spec spec--hair-b">HAIR</p>

    <svg class="free-from-seal" viewBox="0 0 106 106" role="img" aria-label="Free-from seal">
      <circle cx="53" cy="53" r="50" fill="none" stroke="#1f2b2a" stroke-width="2"/>
    </svg>

    <p class="volume">32 fl. oz/ 946 ml</p>
  </section>
</div>
</body>
</html>
```